Custom Anatomical Healing Abutment Flyer

Need a Flyer (4x6 inch) color printed suffer for orders..
See attachment for what I'm looking for. just need it to look Nice (eye candy)...

- reduce the number of steps to 5 (pictures included)

you can remove the watermark (have approval from him to use this) just need to add "permission from volminest"

- Tag Line: (can change the wording if needed)
Custom Anatomical Healing Abutment
Available in Silicone and 3D printed

Target Market(s)

Letting customers know of new product available.

Font styles to use
Sans Serif

Colors

Designer to choose colors to be used in the design.

Requirements
Must have
• - reduce the number of steps to 5 (pictures included)
• you can remove the watermark (have approval from him to use this) just need to add "permission from volminest"
Nice to have
• - Tag Line: (can change the wording if needed)
• Custom Anatomical Healing Abutment
• Available in Silicone and 3D printed

```html
<!DOCTYPE html>
<html lang="en">
<head>
<meta charset="utf-8">
<title>Custom Anatomical Healing Abutment Flyer</title>
<link href="https://fonts.googleapis.com/css2?family=Roboto:wght@400;900&family=Roboto+Condensed:wght@400&display=swap" rel="stylesheet">
<style>
  :root {
    --bg: #e9e7e4;
    --grey-light: #dcdcdc;
    --grey-mid: #b9b9b9;
    --ink: #111111;
    --band: #1c1c1c;
    --band-edge: #2c2c2c;
    --white: #ffffff;
    --ring: #3a3a3a;
  }
  * { margin: 0; padding: 0; box-sizing: border-box; }
  html, body {
    width: 1200px; height: 984px; overflow: hidden;
    background: var(--bg);
  }
  .flyer {
    position: absolute; left: 310px; top: 57px;
    width: 580px; height: 870px;
    background: linear-gradient(160deg, var(--grey-light), var(--grey-mid));
    box-shadow: 0 10px 30px rgba(0,0,0,.25);
    overflow: hidden;
  }
  .process { position: absolute; left: 0; top: 0; width: 580px; height: 580px; }
  .tagline {
    position: absolute; left: 0; top: 570px; width: 580px; height: 300px;
    background: linear-gradient(180deg, var(--band-edge), var(--band));
    color: var(--white); text-align: center;
    padding-top: 46px;
  }
  .tagline__title {
    font-family: "Roboto", sans-serif; font-weight: 900;
    font-size: 38px; line-height: 44px; letter-spacing: .5px;
    text-transform: uppercase;
  }
  .tagline__sub {
    font-family: "Roboto Condensed", sans-serif; font-weight: 400;
    font-size: 36px; line-height: 44px; text-transform: uppercase;
  }
  .tagline__big {
    font-family: "Roboto", sans-serif; font-weight: 900;
    font-size: 66px; line-height: 72px; text-transform: uppercase;
  }
  .credit { font-family: "Roboto", sans-serif; font-size: 12px; fill: var(--white); }
  .badge-num { font-family: "Roboto", sans-serif; font-weight: 900; font-size: 16px; fill: var(--ink); }
</style>
</head>
<body>
<div class="flyer">
  <svg class="process" viewBox="0 0 580 580" xmlns="http://www.w3.org/2000/svg">
    <defs>
      <radialGradient id="tray" cx="50%" cy="50%" r="70%">
        <stop offset="0" stop-color="#a9b0ba"/><stop offset="1" stop-color="#7f8894"/>
      </radialGradient>
      <radialGradient id="dark" cx="50%" cy="50%" r="60%">
        <stop offset="0" stop-color="#555"/><stop offset="1" stop-color="#111"/>
      </radialGradient>
      <radialGradient id="blue" cx="50%" cy="50%" r="60%">
        <stop offset="0" stop-color="#4b5f9e"/><stop offset="1" stop-color="#2f3e4d"/>
      </radialGradient>
      <radialGradient id="mouth" cx="50%" cy="50%" r="60%">
        <stop offset="0" stop-color="#e6c7c3"/><stop offset="1" stop-color="#b8767f"/>
      </radialGradient>
      <radialGradient id="glove" cx="50%" cy="50%" r="60%">
        <stop offset="0" stop-color="#7fa8a2"/><stop offset="1" stop-color="#4d6c72"/>
      </radialGradient>
      <marker id="arrow" viewBox="0 0 10 10" refX="5" refY="5" markerWidth="8" markerHeight="8" orient="auto">
        <path d="M0 1 L10 5 L0 9 L3 5 Z" fill="var(--ink)"/>
      </marker>
    </defs>

    <circle class="cycle-ring" cx="290" cy="300" r="220" fill="none" stroke="var(--ring)" stroke-width="1.5"/>
    <path d="M345 88 A220 220 0 0 1 430 130" fill="none" stroke="none" marker-end="url(#arrow)"/>
    <path d="M500 330 A220 220 0 0 1 490 378" fill="none" stroke="none" marker-end="url(#arrow)"/>
    <path d="M320 517 A220 220 0 0 1 280 520" fill="none" stroke="none" marker-end="url(#arrow)"/>
    <path d="M95 400 A220 220 0 0 1 80 370" fill="none" stroke="none" marker-end="url(#arrow)"/>
    <path d="M160 125 A220 220 0 0 1 200 100" fill="none" stroke="none" marker-end="url(#arrow)"/>

    <circle class="hub" cx="290" cy="300" r="190" fill="var(--ink)"/>
    <rect role="img" aria-label="Silicone tray of anatomical healing abutment moulds" x="150" y="215" width="280" height="120" rx="4" fill="url(#tray)"/>
    <text class="credit" x="290" y="362" text-anchor="middle">Permission from VOLMINEST</text>

    <g class="step">
      <circle role="img" aria-label="Abutment mounted on a handle" cx="290" cy="80" r="62" fill="url(#dark)"/>
      <circle cx="350" cy="40" r="16" fill="var(--white)" stroke="var(--ink)" stroke-width="1.5"/>
      <text class="badge-num" x="350" y="46" text-anchor="middle">1</text>
    </g>
    <g class="step">
      <circle role="img" aria-label="Filling a mould in the silicone tray" cx="499" cy="232" r="62" fill="url(#glove)"/>
      <circle cx="530" cy="180" r="16" fill="var(--white)" stroke="var(--ink)" stroke-width="1.5"/>
      <text class="badge-num" x="530" y="186" text-anchor="middle">2</text>
    </g>
    <g class="step">
      <circle role="img" aria-label="Light curing the mould" cx="419" cy="478" r="62" fill="url(#blue)"/>
      <circle cx="470" cy="440" r="16" fill="var(--white)" stroke="var(--ink)" stroke-width="1.5"/>
      <text class="badge-num" x="470" y="446" text-anchor="middle">3</text>
    </g>
    <g class="step">
      <circle role="img" aria-label="Abutment placed in the mouth" cx="161" cy="478" r="62" fill="url(#mouth)"/>
      <circle cx="118" cy="510" r="16" fill="var(--white)" stroke="var(--ink)" stroke-width="1.5"/>
      <text class="badge-num" x="118" y="516" text-anchor="middle">4</text>
    </g>
    <g class="step">
      <circle role="img" aria-label="Healed gum contour around implant" cx="81" cy="232" r="62" fill="url(#mouth)"/>
      <circle cx="32" cy="190" r="16" fill="var(--white)" stroke="var(--ink)" stroke-width="1.5"/>
      <text class="badge-num" x="32" y="196" text-anchor="middle">5</text>
    </g>
  </svg>

  <div class="tagline">
    <p class="tagline__title">Custom Anatomical</p>
    <p class="tagline__title">Healing Abutment</p>
    <p class="tagline__sub">Available in Silicone &amp;</p>
    <p class="tagline__big">3D Printed</p>
  </div>
</div>
</body>
</html>
```